Design some Business Cards for Vellor Motion

Vellor Motion, an automation design and services company specializing in packaging equipment in manufacturing facilities is in need of an updated business card design. I've got 3 different variations on the logo which I've attached. The primary hex colors are:

53D41D >> green
666666 >> grey

For the business cards, we'd like a 2-sided card. The info side should include:
- employee name
- title
- company name
- company address (6120 Fenwick Court, York, PA 17408)
- phone (both +1.717.555.0143 and 800.555.0178)
- e-mail

The web address [login to view URL] should appear somewhere on the card but I'll leave it up to you for the placement.

The color green should be highlighted on at least one side of the card. The logo cannot be altered in color or layout from the files provided.

PLEASE LIMIT YOUR SUBMISSIONS TO A MAXIMUM OF 12 DESIGNS.

I look forward to seeing the results.

Thanks in advance,
Marlene

```html
<!DOCTYPE html>
<html lang="en">
<head>
<meta charset="utf-8">
<title>Vellor Motion — Business Card</title>
<link rel="stylesheet" href="https://fonts.googleapis.com/css2?family=Exo+2:wght@500&family=Open+Sans:wght@400;700&display=swap">
<style>
  :root {
    --green: #53d41d;
    --grey: #666666;
    --white: #ffffff;
    --backdrop: #ecebe8;
  }
  * { box-sizing: border-box; margin: 0; padding: 0; }
  html, body { width: 1200px; height: 715px; overflow: hidden; }
  body {
    background: var(--backdrop);
    font-family: "Open Sans", Arial, sans-serif;
    position: relative;
  }
  .card {
    position: absolute;
    top: 208px;
    width: 520px;
    height: 298px;
    overflow: hidden;
    box-shadow: 0 6px 18px rgba(0,0,0,.18);
  }
  .card--front { left: 50px; background: var(--white); }
  .card--back {
    left: 630px;
    background: var(--grey);
    display: flex;
    align-items: center;
    justify-content: center;
    padding: 0 48px;
  }

  .brand { display: flex; align-items: center; gap: 14px; }
  .brand__dot { width: 56px; height: 56px; border-radius: 50%; flex: none; }
  .brand__name {
    font-family: "Exo 2", Arial, sans-serif;
    font-weight: 500;
    letter-spacing: 2px;
    text-transform: uppercase;
    white-space: nowrap;
  }

  .front__head { height: 118px; padding: 0 0 0 34px; display: flex; align-items: center; }
  .front__head .brand__dot { background: var(--grey); }
  .front__head .brand__name { color: var(--green); font-size: 42px; }

  .front__band {
    height: 58px;
    background: var(--green);
    text-align: center;
    color: var(--white);
    padding-top: 9px;
  }
  .person__name { font-weight: 700; font-size: 17px; letter-spacing: 1px; text-transform: uppercase; line-height: 1.2; }
  .person__title { font-size: 12px; line-height: 1.4; }

  .front__contact {
    height: 122px;
    background: var(--grey);
    display: grid;
    grid-template-columns: repeat(3, 1fr);
    padding: 18px 18px 0;
    color: var(--white);
    font-size: 11.5px;
    line-height: 1.55;
  }
  .contact-item { display: flex; flex-direction: column; align-items: center; text-align: center; gap: 10px; }
  .contact-item svg { width: 30px; height: 30px; }

  .card--back .brand { gap: 16px; }
  .card--back .brand__dot { background: var(--white); width: 64px; height: 64px; }
  .card--back .brand__name { color: var(--white); font-size: 40px; }
</style>
</head>
<body>
  <section class="card card--front" aria-label="Business card, info side">
    <header class="front__head">
      <div class="brand">
        <span class="brand__dot"></span>
        <span class="brand__name">Vellor Motion</span>
      </div>
    </header>
    <div class="front__band">
      <p class="person__name">Dorian Maksell</p>
      <p class="person__title">Automation Technician</p>
    </div>
    <div class="front__contact">
      <div class="contact-item">
        <svg viewBox="0 0 24 24" aria-hidden="true"><path fill="#53d41d" d="M6.6 10.8a15.1 15.1 0 0 0 6.6 6.6l2.2-2.2a1 1 0 0 1 1-.25 11.4 11.4 0 0 0 3.6.57 1 1 0 0 1 1 1V20a1 1 0 0 1-1 1A17 17 0 0 1 3 4a1 1 0 0 1 1-1h3.5a1 1 0 0 1 1 1c0 1.25.2 2.45.57 3.570a1 1 0 0 1-.25 1z"/></svg>
        <p>+1.717.555.0143<br>800.555.0178</p>
      </div>
      <div class="contact-item">
        <svg viewBox="0 0 24 24" aria-hidden="true"><circle cx="12" cy="12" r="10" fill="#53d41d"/><path fill="none" stroke="#666" stroke-width="1.4" d="M2 12h20M12 2c3 3 3 17 0 20M12 2c-3 3-3 17 0 20"/></svg>
        <p>dorian@vellormotion.com<br>www.vellormotion.com</p>
      </div>
      <div class="contact-item">
        <svg viewBox="0 0 24 24" aria-hidden="true"><path fill="#53d41d" d="M12 2a7 7 0 0 0-7 7c0 5.2 7 13 7 13s7-7.8 7-13a7 7 0 0 0-7-7zm0 9.5A2.5 2.5 0 1 1 12 6.5a2.5 2.5 0 0 1 0 5z"/></svg>
        <p>6120 Fenwick Court<br>York, PA 17408</p>
      </div>
    </div>
  </section>

  <section class="card card--back" aria-label="Business card, logo side">
    <div class="brand">
      <span class="brand__dot"></span>
      <span class="brand__name">Vellor Motion</span>
    </div>
  </section>
</body>
</html>
```